Gif animated banner ads for Vexaro and Social Media ads for PageLoomly.com

Please make banner ads to promote PageLoomly's new Affiliate Program. PageLoomly is an AI Website Builder that instantly generates beautiful websites for all types of businesses.

I prefer gif animated banners, but I am open to non-animated banners if they look great and you don't offer gifs.

The points to focus on for the content are:
A. Every business needs a website
B. They earn BIG commissions by referring the #1 website builder platform, PageLoomly.com
C. PageLoomly pays 30% recurring commission on every sale
D. Affiliate program is through AllyHarbor, a trusted Affiliate Platform

Obviously, you won't be able to include all that content on each banner, especially since some are fairly small in size. However, please be creative and try to hit the bullet points that will get the viewer's attention.

I need the banner ads made in 26 sizes as follows:
200 × 200
240 × 400
250 × 250
250 × 360
300 × 250
336 × 280
580 × 400
120 × 600
160 × 600
300 × 600
300 × 1050
468 × 60
728 × 90
930 × 180
970 × 90
970 × 250
980 × 120
300 × 50
320 × 50
320 × 100
1200 x 620
1080 x 1080
1200 x 1200
720 x 1280
1280 x 720
640 x 640

I have attached some variations of the PageLoomly logo. Feel free to incorporate it into your banners.

I look forward to seeing your work!

Target Market(s)

Businesses

Industry/Entity Type

Technology, Internet, Artificial Intelligence (AI)

Colors
0054AA
0677BA
7BADD7
CADEEF
E8F1F8

Requirements
Must have
• Must be eye-catching

```html
<!DOCTYPE html>
<html lang="en">
<head>
<meta charset="utf-8">
<title>PageLoomly – Every Business Needs a Website – 1080 x 1080</title>
<link rel="stylesheet" href="https://fonts.googleapis.com/css2?family=Poppins:wght@500;600;700&display=swap">
<style>
  :root {
    --board-grey: #d4d4d4;
    --label-ink: #0e1a2e;
    --navy: #0b0d5c;
    --sky-start: #0a8cff;
    --sky-end: #2bc3e2;
    --wave-start: #13b4dc;
    --wave-end: #0c7fe0;
    --photo-deep: #050f17;
    --photo-mid: #0b2f40;
    --photo-glow: #2aa9c9;
    --photo-light: #8fb3c4;
    --photo-warm: #b5652a;
    --white: #ffffff;
  }
  * { margin: 0; padding: 0; box-sizing: border-box; }
  html, body {
    width: 1200px;
    height: 1156px;
    overflow: hidden;
    background: var(--board-grey);
    font-family: "Poppins", sans-serif;
  }
  .size-label {
    position: absolute;
    left: 118px;
    top: 61px;
    font-size: 31px;
    font-weight: 700;
    line-height: 1;
    letter-spacing: 0;
    color: var(--label-ink);
  }
  .banner {
    position: absolute;
    left: 118px;
    top: 117px;
    width: 945px;
    height: 945px;
    overflow: hidden;
    background: var(--white);
  }
  .banner-art {
    position: absolute;
    inset: 0;
    width: 945px;
    height: 945px;
  }
  .brand-name {
    position: absolute;
    right: 38px;
    top: 76px;
    font-size: 66px;
    font-weight: 600;
    line-height: 1;
    letter-spacing: -1px;
    color: var(--white);
  }
  .headline {
    position: absolute;
    left: 0;
    width: 945px;
    text-align: center;
    line-height: 1;
    letter-spacing: -0.5px;
  }
  .headline-top {
    top: 735px;
    font-size: 92px;
    font-weight: 500;
    color: var(--navy);
  }
  .headline-bottom {
    top: 826px;
    font-size: 84px;
    font-weight: 700;
  }
  .headline-bottom span {
    background: linear-gradient(90deg, var(--sky-start), var(--sky-end));
    -webkit-background-clip: text;
    background-clip: text;
    color: transparent;
  }
</style>
</head>
<body>
  <div class="size-label">1080 X 1080</div>

  <section class="banner">
    <svg class="banner-art" viewBox="0 0 1544 1544" xmlns="http://www.w3.org/2000/svg">
      <defs>
        <linearGradient id="photoBase" x1="0" y1="0" x2="1" y2="1">
          <stop offset="0" stop-color="var(--photo-mid)"/>
          <stop offset="0.6" stop-color="var(--photo-deep)"/>
          <stop offset="1" stop-color="var(--photo-mid)"/>
        </linearGradient>
        <radialGradient id="photoGlow" cx="0.28" cy="0.38" r="0.45">
          <stop offset="0" stop-color="var(--photo-glow)" stop-opacity="0.85"/>
          <stop offset="1" stop-color="var(--photo-glow)" stop-opacity="0"/>
        </radialGradient>
        <radialGradient id="photoLight" cx="0.62" cy="0.78" r="0.4">
          <stop offset="0" stop-color="var(--photo-light)" stop-opacity="0.55"/>
          <stop offset="1" stop-color="var(--photo-light)" stop-opacity="0"/>
        </radialGradient>
        <radialGradient id="photoWarm" cx="1" cy="0.05" r="0.25">
          <stop offset="0" stop-color="var(--photo-warm)" stop-opacity="0.6"/>
          <stop offset="1" stop-color="var(--photo-warm)" stop-opacity="0"/>
        </radialGradient>
        <linearGradient id="waveTone" x1="0" y1="0" x2="1" y2="0">
          <stop offset="0" stop-color="var(--wave-start)"/>
          <stop offset="1" stop-color="var(--wave-end)"/>
        </linearGradient>
      </defs>
      <g class="hero-photo" role="img"
         aria-label="Photo of hands typing on a laptop while a glowing holographic AI robot emerges from the screen among blue circuit lines">
        <rect x="0" y="0" width="1544" height="1160" fill="url(#photoBase)"/>
        <rect x="0" y="0" width="1544" height="1160" fill="url(#photoGlow)"/>
        <rect x="0" y="0" width="1544" height="1160" fill="url(#photoLight)"/>
        <rect x="0" y="0" width="1544" height="1160" fill="url(#photoWarm)"/>
      </g>
      <path class="wave-band" d="M0,1084 C200,1000 400,990 700,1040 S1300,1110 1544,955 L1544,1544 L0,1544 Z" fill="url(#waveTone)"/>
      <path class="wave-base" d="M0,1092 C250,1030 450,1060 700,1110 S1300,1190 1544,980 L1544,1544 L0,1544 Z" fill="var(--white)"/>
    </svg>

    <div class="brand-name">PageLoomly</div>

    <h1 class="headline headline-top">EVERY BUSINESS</h1>
    <h2 class="headline headline-bottom"><span>NEEDS A WEBSITE</span></h2>
  </section>
</body>
</html>
```